Werbeflyer/Werbepostkarte für kleines Einzelunternehmen
Hallo Zusammen,
wir sind ein junges Unternehmen, welches überwiegend bayrische Accessoires designen und anfertigen. Unsere Zielgruppe sind sowohl Einzelhändler als auch der Endverbraucher. Insbesondere die feierwütige Gesellschaft der Volksfeste.
Da wir noch recht unbekannt sind, wollen wir durch die Flyer unseren Bekanntheitsgrad steigern und die Flyer auf Volksfesten oder im Einzelhandel verteilen/auslegen lassen.
Aufgabenstellung
Wir stellen uns einen Werbeflyer in Postkartenformat (A6) vor, der beidseitig bedruckt ist. Auf der Vorderseite sollen unsere Produkte so präsentiert werden, dass deutlich wird, was dieses Produkt darstellt und wofür es verwendet werden soll. Dabei beziehe ich mich vor allem auf die "Zwirnel-Ringe", welche zum einen als modisches Accessoires am Handgelenk fundieren und zum anderen als Bierkrug-Markierband. (Produktbilder sind dem Anhang beigefügt)
Zusätzlich soll ein schlichter Schriftzug darauf aufmerksam machen, dass man sich die Zwirnel-Ringe selber generieren/zusammenstellen/designen lassen kann, sodass sie zu jeder Tracht bzw. zu jedem Outfit individuell passen.
Gerne würden wir auch noch die Schlüsselbänder (ein Bild ist ausreichend) mit unterbringen, sodass erkenntlich wird, dass wir nicht nur die Zwirnel-Ringe produzieren, sondern auch andere bayerisch-angehauchte Accessoires.
Zum Schluss soll unser Logo noch mit untergebracht werden.
Die Rückseite soll schlicht gehalten werden und das Layout einer Postkartenrückseite abbilden. Ein Hinweis auf die Firma ( Logo, Adresse, Telefon, E-Mailadresse, Internetadresse) soll ebenfalls abgebildet werden.
Das ganze Design sollte insgesamt sehr schlicht und vintagemäßig von der Farbwahl gehalten werden. Am schönsten wäre es, wenn der Flyer durch sein Design den Zweck einer Postkarte erfüllt und verschickt wird.
Sollten sie noch weitere Materialien, Bilder, etc. benötigen oder noch offene Fragen zu meinen Angaben sind, bitte ich Sie mich einfach zu kontaktieren.
Vielen lieben Dank schonmal im Voraus.

```html
<!DOCTYPE html>
<html lang="de">
<head>
<meta charset="utf-8">
<title>Wiesl Werk – Postkarte Vorder- und Rückseite</title>
<link rel="stylesheet" href="https://fonts.googleapis.com/css2?family=Open+Sans:wght@400;600&family=Allura&display=swap">
<style>
  :root{
    --canvas:#ffffff;
    --wood-light:#d6d0c9;
    --wood-dark:#b8b0a7;
    --lilac:#a686bd;
    --lilac-band:#b594cb;
    --taupe:#b9aa9b;
    --taupe-line:#cfc3b6;
    --stamp:#e8e5e2;
    --white:#ffffff;
    --ink:#3a3a3a;
  }
  *{box-sizing:border-box;margin:0;padding:0}
  html,body{width:1200px;height:848px;overflow:hidden;background:var(--canvas)}
  body{position:relative;font-family:"Open Sans",sans-serif}

  .card{position:absolute;width:560px;height:400px;top:224px;box-shadow:0 2px 6px rgba(0,0,0,.18);overflow:hidden}
  .card--front{left:30px}
  .card--back{left:610px;background:var(--white)}

  /* front */
  .wood{position:absolute;inset:0;background:linear-gradient(160deg,var(--wood-light),var(--wood-dark))}
  .photo{position:absolute;border:4px solid var(--white)}
  .photo--mug{left:-4px;top:-4px;width:164px;height:264px;background:linear-gradient(135deg,#d7d3cd,#8f877d 60%,#c6b8d6)}
  .photo--cuff{left:273px;top:180px;width:118px;height:168px;background:linear-gradient(180deg,#ece9e5,#bcb2a6 55%,#c9b6d8)}
  .path{position:absolute;inset:0}
  .badge{position:absolute;left:132px;top:18px;width:136px;height:136px;border-radius:50%;background:var(--white);display:flex;align-items:center;justify-content:center;z-index:2}
  .badge__name{font-weight:600;font-size:20px;color:var(--ink)}
  .headline{position:absolute;left:282px;top:20px;width:270px;text-align:center;color:var(--white);z-index:2}
  .headline__lead{font-size:17px;font-weight:600;letter-spacing:.3px}
  .headline__product{font-family:"Allura",cursive;font-size:52px;line-height:1.05;color:var(--lilac);white-space:nowrap;margin-top:2px}
  .headline__tag{font-size:14px;margin-top:4px;white-space:nowrap}
  .step{position:absolute;width:64px;height:64px;border-radius:50%;background:var(--white);border:2px dotted #555;display:flex;align-items:center;justify-content:center;z-index:3}
  .step--one{left:139px;top:197px}
  .step--two{left:372px;top:150px}
  .step__art{width:44px;height:44px;border-radius:50%;background:#ecebe9}
  .step__num{position:absolute;width:22px;height:22px;border-radius:50%;background:var(--white);border:1px solid #555;font-size:12px;display:flex;align-items:center;justify-content:center;color:var(--ink)}
  .step--one .step__num{left:-14px;top:40px}
  .step--two .step__num{left:-10px;top:46px}
  .note{position:absolute;font-size:12.5px;line-height:19px;color:var(--white);z-index:1}
  .note span{background:var(--lilac-band);padding:0 4px;box-decoration-break:clone;-webkit-box-decoration-break:clone}
  .note--mug{left:26px;top:278px;width:200px}
  .note--wrist{left:402px;top:262px;width:145px}
  .range{position:absolute;left:0;right:0;bottom:0;height:28px;background:var(--white);display:flex;align-items:center;justify-content:center;gap:10px;font-size:12.5px;letter-spacing:1.2px;color:var(--taupe)}

  /* back */
  .frame{position:absolute;inset:8px;border:1px dotted var(--taupe-line)}
  .sender{position:absolute;left:20px;top:22px;display:flex;gap:22px;align-items:flex-start}
  .sender__mark{width:90px;height:90px;border-radius:50%;border:1px solid var(--taupe-line);display:flex;align-items:center;justify-content:center;font-size:13px;font-weight:600;color:var(--taupe-line)}
  .sender__address{font-size:10px;line-height:13px;color:var(--taupe);margin-top:24px;font-style:normal}
  .sender__web{font-weight:600}
  .stamp{position:absolute;right:20px;top:20px;width:70px;height:92px;background:var(--stamp);border:2px dotted var(--white);outline:1px solid var(--stamp)}
  .divider{position:absolute;left:280px;top:152px;width:4px;height:188px;background:var(--taupe-line)}
  .address-line{position:absolute;left:300px;width:238px;height:1px;background:var(--taupe-line)}
  .range-small{position:absolute;left:18px;top:328px;font-size:9.5px;color:var(--taupe);white-space:nowrap}
</style>
</head>
<body>

<section class="card card--front" aria-label="Postkarte Vorderseite">
  <div class="wood" role="img" aria-label="Heller Holzdielen-Hintergrund"></div>
  <div class="photo photo--mug" role="img" aria-label="Foto: Zwirnel-Ring am Henkel eines Bierkrugs"></div>

  <svg class="path" viewBox="0 0 560 400" aria-hidden="true">
    <path d="M190 215 C 230 175, 300 165, 380 180 S 500 170, 560 150" fill="none" stroke="#333" stroke-width="1.4" stroke-dasharray="1.5 3"/>
  </svg>

  <div class="photo photo--cuff" role="img" aria-label="Foto: Zwirnel-Ring als Armband getragen"></div>

  <div class="badge"><span class="badge__name">Wiesl Werk</span></div>

  <div class="headline">
    <p class="headline__lead">Designe deine eigenen</p>
    <p class="headline__product">Zwirnel-Ringe</p>
    <p class="headline__tag">. . . passend zu Deiner Tracht!</p>
  </div>

  <div class="step step--one">
    <div class="step__art" role="img" aria-label="Zeichnung eines Bierkrugs"></div>
    <span class="step__num">1.</span>
  </div>
  <div class="step step--two">
    <div class="step__art" role="img" aria-label="Zeichnung eines Handgelenks mit Armband"></div>
    <span class="step__num">2.</span>
  </div>

  <p class="note note--mug"><span>Mit Hilfe der kleinen Bänder erkennt man auch im dichtesten Bierkrug-getümmel seine Maß auf dem Tisch.</span></p>
  <p class="note note--wrist"><span>Und nach dem Genuß wird es einfach als modisches Accessoires um das Handgelenk geschlungen.</span></p>

  <p class="range"><span>ZWIRNEL-RINGE</span><span>|</span><span>SCHLÜSSELANHÄNGER</span><span>|</span><span>HUNDEHALSBÄNDER</span></p>
</section>

<section class="card card--back" aria-label="Postkarte Rückseite">
  <div class="frame"></div>
  <div class="sender">
    <div class="sender__mark">Wiesl Werk</div>
    <address class="sender__address">
      Ahornweg 14<br>
      80999 Musterstadt<br>
      info@wieslwerk.example<br>
      <span class="sender__web">www.wieslwerk.example</span>
    </address>
  </div>
  <div class="stamp"></div>
  <div class="divider"></div>
  <div class="address-line" style="top:190px"></div>
  <div class="address-line" style="top:231px"></div>
  <div class="address-line" style="top:269px"></div>
  <div class="address-line" style="top:310px"></div>
  <p class="range-small">Zwirnel-Ringe | Schlüsselanhänger | Hundehalsbänder</p>
</section>

</body>
</html>
```